Re-branding for Structural Engineering firm

We need new business cards as part of our current re-branding. We have a new logo (attached), so the card design should incorporate this color scheme. We are a structural engineering firm providing structural building design and seismic consulting services. The final design should communicate professionalism and stability, with a modern look and feel.

```html
<!DOCTYPE html>
<html lang="en">
<head>
<meta charset="utf-8">
<title>RVN Structural Engineering – Business Card</title>
<link rel="stylesheet" href="https://fonts.googleapis.com/css2?family=Roboto:wght@400;700;900&family=Antonio:wght@400&display=swap">
<style>
  :root {
    --stage-light: #ffffff;
    --stage-edge: #e9eaeb;
    --card-white: #ffffff;
    --brand-blue: #317ac1;
    --icon-blue: #1f9ad3;
    --brand-gray: #898a8c;
    --card-border: #dfe3e8;
  }
  html, body {
    margin: 0;
    width: 1200px;
    height: 1200px;
    overflow: hidden;
  }
  body {
    background: radial-gradient(circle at 50% 50%, var(--stage-light) 0%, var(--stage-light) 30%, var(--stage-edge) 100%);
    position: relative;
  }
  .business-card {
    position: absolute;
    left: 200px;
    top: 350px;
    width: 802px;
    height: 501px;
    display: block;
  }
  .card-base { fill: var(--card-white); stroke: var(--card-border); stroke-width: 1; }
  .blue-panel { fill: var(--brand-blue); }
  .icon-notch { fill: var(--card-white); }
  .speed-stripe { fill: var(--card-white); }
  .contact-icon { fill: var(--icon-blue); }
  .brand-mark { fill: var(--brand-blue); }
  .brand-name {
    font-family: "Roboto", sans-serif;
    font-weight: 700;
    font-size: 54px;
    fill: var(--brand-blue);
  }
  .brand-descriptor {
    font-family: "Roboto", sans-serif;
    font-weight: 700;
    font-size: 16px;
    fill: var(--brand-blue);
  }
  .brand-url {
    font-family: "Roboto", sans-serif;
    font-size: 16px;
    fill: var(--brand-gray);
  }
  .tagline {
    font-family: "Antonio", sans-serif;
    font-size: 30px;
    fill: var(--brand-blue);
  }
  .person-name {
    font-family: "Roboto", sans-serif;
    font-weight: 900;
    font-size: 31px;
    fill: var(--card-white);
    letter-spacing: 1px;
  }
  .person-title {
    font-family: "Roboto", sans-serif;
    font-size: 25px;
    fill: var(--card-white);
  }
  .contact-text {
    font-family: "Roboto", sans-serif;
    font-size: 25px;
    fill: var(--card-white);
  }
</style>
</head>
<body>
<svg class="business-card" viewBox="0 0 802 501" xmlns="http://www.w3.org/2000/svg" role="img" aria-label="RVN Structural Engineering business card for Marcus Bell">
  <rect class="card-base" x="0.5" y="0.5" width="801" height="500"/>
  <polygon class="blue-panel" points="434,0 802,0 802,501 209,501"/>

  <!-- icon notches along the diagonal -->
  <polygon class="icon-notch" points="304,205 321,177 353,177 370,205 353,233 321,233"/>
  <polygon class="icon-notch" points="274,277 291,249 323,249 340,277 323,305 291,305"/>
  <polygon class="icon-notch" points="244,348 261,320 293,320 310,348 293,376 261,376"/>
  <polygon class="icon-notch" points="214,420 231,392 263,392 280,420 263,448 231,448"/>

  <!-- contact icons -->
  <path class="contact-icon" d="M337,189 l-18,16 h5 v16 h9 v-9 h8 v9 h9 v-16 h5 z"/>
  <g class="contact-icon">
    <rect x="292" y="267" width="31" height="21" rx="1"/>
    <path d="M293,268 l14.5,12 l14.5,-12" fill="none" stroke="#ffffff" stroke-width="2"/>
  </g>
  <path class="contact-icon" d="M268,335 c-3,1 -4,4 -3,9 c2,8 8,15 15,18 c4,2 8,1 10,-2 l-6,-6 l-4,3 c-4,-2 -7,-6 -8,-10 l3,-4 z"/>
  <path class="contact-icon" d="M247,404 a12,12 0 0 1 12,12 c0,9 -12,22 -12,22 c0,0 -12,-13 -12,-22 a12,12 0 0 1 12,-12 z M247,411 a5,5 0 1 0 0.01,0 z" fill-rule="evenodd"/>

  <!-- speed stripes -->
  <rect class="speed-stripe" x="747" y="362" width="55" height="11"/>
  <rect class="speed-stripe" x="687" y="386" width="115" height="11"/>
  <rect class="speed-stripe" x="725" y="412" width="77" height="11"/>
  <rect class="speed-stripe" x="743" y="438" width="59" height="11"/>

  <!-- brand block -->
  <rect class="brand-mark" x="61" y="80" width="44" height="44"/>
  <text class="brand-name" x="114" y="124">RVN</text>
  <text class="brand-descriptor" x="61" y="175">STRUCTURAL</text>
  <text class="brand-descriptor" x="61" y="192">ENGINEERING</text>
  <text class="brand-url" x="61" y="216">www.rvnse.com</text>

  <!-- tagline -->
  <text class="tagline" x="197" y="345" text-anchor="end">PRECISION</text>
  <text class="tagline" x="197" y="376" text-anchor="end">STRENGTH</text>
  <text class="tagline" x="197" y="407" text-anchor="end">VISION</text>

  <!-- person -->
  <text class="person-name" x="740" y="92" text-anchor="end">MARCUS BELL</text>
  <text class="person-title" x="740" y="125" text-anchor="end">Director</text>

  <!-- contact details -->
  <text class="contact-text" x="392" y="213">4410 Harbor Ridge Drive,</text>
  <text class="contact-text" x="392" y="245">Suite 210 San Diego, CA 92127</text>
  <text class="contact-text" x="359" y="296">info@rvnse.com</text>
  <text class="contact-text" x="322" y="365">858.555.0142</text>
  <text class="contact-text" x="295" y="435">www.rvnse.com</text>
</svg>
</body>
</html>
```